Design for online reviews widget

Attached is a wireframe of a widget we need designing to display reviews on websites from multiple sources. We need this provided at 3 different sizes including full screen, contained (like the wireframe) and mobile.
You have completely free rein on the styling.
The only elements that should remain untouched are the blue stars (https://www.filquarry.net/s/8vtmwp2291zq4h/kv%20stars.ai?dl=0) and powered by logo at the bottom.
Ignore the menu at the top of the wireframe, this is just from the website the widget will be placed on.
Businesses

```html
<!DOCTYPE html>
<html lang="en">
<head>
<meta charset="utf-8">
<title>Reviews Widget</title>
<link href="https://fonts.googleapis.com/css2?family=Roboto:wght@300;400;500;700&display=swap" rel="stylesheet">
<style>
:root{
  --bg:#f4f4f4;
  --card:#ffffff;
  --ink:#111111;
  --body:#555555;
  --green:#5a9e2f;
  --gold:#f2c200;
  --blue:#2bb3e6;
  --score:#0b4f8f;
  --footer:#1e1e1e;
  --muted:#888888;
}
*{margin:0;padding:0;box-sizing:border-box}
html,body{width:879px;height:1200px;overflow:hidden}
body{background:var(--bg);font-family:'Roboto',sans-serif;position:relative;color:var(--ink)}
.score{position:absolute;left:0;width:879px;top:44px;text-align:center}
.score-stars{display:flex;justify-content:center;gap:4px}
.score-stars svg{width:19px;height:19px}
.score-text{font-size:11px;margin-top:4px}
.sort{position:absolute;left:645px;top:47px;width:152px;height:31px;background:#fff;border:1px solid #e2e2e2;border-radius:3px;font-size:10.5px;display:flex;align-items:center;padding-left:15px}
.sort b{font-weight:500;margin-right:6px}
.sort span{color:var(--muted)}
.sort svg{position:absolute;right:13px;top:13px;width:7px;height:5px}
.review{position:absolute;left:83px;width:713px;height:193px;background:var(--card);border-radius:4px;box-shadow:0 1px 6px rgba(0,0,0,.08);padding:17px 132px 0 20px}
.review h2{font-size:12px;font-weight:500;margin-bottom:9px}
.review p{font-size:10.2px;font-weight:300;color:var(--body);line-height:18.8px}
.review .service{color:var(--ink);font-weight:400}
.author{position:absolute;left:20px;bottom:14px;display:flex;align-items:center}
.avatar{width:35px;height:35px;margin-right:12px}
.author-name{font-size:10.5px;font-weight:500;color:var(--green)}
.author-name small{font-size:9px;font-weight:400}
.stars{display:flex;gap:2px;margin-top:5px}
.stars svg{width:11px;height:11px;fill:var(--gold)}
.source{position:absolute;right:21px;top:0;bottom:0;width:90px;display:flex;flex-direction:column;align-items:center;justify-content:center;gap:7px}
.source-name{font-size:12px;font-weight:500;color:var(--ink)}
.source .stars svg{width:10px;height:10px}
.source-score{font-size:16px;font-weight:700;color:var(--score)}
.load{position:absolute;left:381px;top:1054px;width:117px;height:38px;background:var(--green);border-radius:4px;color:#fff;font-size:12px;font-weight:500;display:flex;align-items:center;justify-content:center;gap:6px}
.load svg{width:11px;height:11px}
.powered{position:absolute;left:625px;top:1068px;display:flex;align-items:center;gap:8px}
.powered i{width:34px;height:34px;border-radius:50%;background:var(--blue);display:block}
.powered-by{font-size:13px;color:#555}
.powered-name{font-size:19px;font-weight:700;color:var(--ink);line-height:1}
.footer{position:absolute;left:0;top:1162px;width:879px;height:38px;background:var(--footer);color:#fff;font-size:10px;display:flex;align-items:center;justify-content:center}
</style>
</head>
<body>
<svg width="0" height="0" style="position:absolute">
  <symbol id="star" viewBox="0 0 24 24"><path d="M12 2l2.9 6.6 7.1.6-5.4 4.7 1.6 7-6.2-3.7-6.2 3.7 1.6-7L2 9.2l7.1-.6z"/></symbol>
  <symbol id="badge-star" viewBox="0 0 24 24"><circle cx="12" cy="12" r="12" fill="#2bb3e6"/><circle cx="12" cy="12" r="9.5" fill="none" stroke="#fff" stroke-width="1.2"/><path fill="#fff" d="M12 5.5l1.8 4.1 4.4.4-3.3 2.9 1 4.3-3.9-2.3-3.9 2.3 1-4.3-3.3-2.9 4.4-.4z"/></symbol>
  <symbol id="user" viewBox="0 0 36 36"><circle cx="18" cy="18" r="17" fill="#fff" stroke="#bbb" stroke-width="2"/><circle cx="18" cy="14" r="6" fill="#bbb"/><path d="M7 29c2-6 6-8 11-8s9 2 11 8" fill="#bbb"/></symbol>
</svg>

<section class="score">
  <div class="score-stars">
    <svg><use href="#badge-star"/></svg><svg><use href="#badge-star"/></svg><svg><use href="#badge-star"/></svg><svg><use href="#badge-star"/></svg><svg><use href="#badge-star"/></svg>
  </div>
  <div class="score-text">Combined Review Score 4.3 out of 5</div>
</section>

<div class="sort"><b>Sort by:</b><span>Most helpful</span><svg viewBox="0 0 8 5"><path d="M0 0h8L4 5z" fill="#222"/></svg></div>

<article class="review" style="top:130px">
  <h2>Front door with windows each side and side window</h2>
  <p>This is the second time we have used Monarch Home Improvements , and the service is amazing! Owen came round several times as we keep changing our minds and he was so helpful and gave us good advice, and the guys who do the fitting are efficient and tidy . I’ve got to say the end result is amazing and I have recommended to many of friends Thanks Monarch Reliablity: 9.38 Courtesy: 10 Tidiness: 9.84 Workmanship: 10</p>
  <div class="author"><svg class="avatar"><use href="#user"/></svg><div><div class="author-name">By Hartfield, <small>28th September 2021</small></div><div class="stars"><svg><use href="#star"/></svg><svg><use href="#star"/></svg><svg><use href="#star"/></svg><svg><use href="#star"/></svg><svg><use href="#star"/></svg></div></div></div>
  <div class="source"><div class="source-name">TradeCheck</div><div class="source-score">9.77</div></div>
</article>

<article class="review" style="top:354px">
  <h2>Positive: Professionalism, Quality, Value</h2>
  <p>The team did a good job of replacing a large feature window spanning two floors, as well as the others in my property. They're a professional group who were willing to work out solutions to any problem, especially compared to other companies. Prices are fair, and my new UPVC windows look great. Special thanks to Frank for being so accommodating and for the good communication throughout.<br><span class="service">Service: Window installation</span></p>
  <div class="author"><svg class="avatar"><use href="#user"/></svg><div><div class="author-name">By Daniel Reeve, <small>11 months ago</small></div><div class="stars"><svg><use href="#star"/></svg><svg><use href="#star"/></svg><svg><use href="#star"/></svg><svg><use href="#star"/></svg><svg><use href="#star"/></svg></div></div></div>
  <div class="source"><div class="source-name" style="font-size:16px">Searchly</div><div class="stars"><svg><use href="#star"/></svg><svg><use href="#star"/></svg><svg><use href="#star"/></svg><svg><use href="#star"/></svg><svg><use href="#star"/></svg></div></div>
</article>

<article class="review" style="top:578px">
  <h2>Brilliant all round professional, friendly service.</h2>
  <p>This home run friendly business was a real pleasure to deal with. From the professional, no pressure quote, nothing was too much trouble to ensure everything is as required for your needs with the quote and fitting. The workmanship and double glazing being fitted was brilliant and my home/outdoors was left tidy and clean leaving an outstanding impression for such an all round professional job. I would not hesitate to recommend this company, such a brilliant service from great hardworking people that care about their service</p>
  <div class="author"><svg class="avatar"><use href="#user"/></svg><div><div class="author-name">By GreenChair42, <small>13 Feb 2018</small></div><div class="stars"><svg><use href="#star"/></svg><svg><use href="#star"/></svg><svg><use href="#star"/></svg><svg><use href="#star"/></svg><svg><use href="#star"/></svg></div></div></div>
  <div class="source"><div class="source-name" style="font-size:16px">Listwell</div><div class="stars"><svg style="width:15px;height:15px"><use href="#star"/></svg><svg style="width:15px;height:15px"><use href="#star"/></svg><svg style="width:15px;height:15px"><use href="#star"/></svg><svg style="width:15px;height:15px"><use href="#star"/></svg><svg style="width:15px;height:15px"><use href="#star"/></svg></div></div>
</article>

<article class="review" style="top:802px">
  <h2>Front door with windows each side and side window.</h2>
  <p>This is the second time we have used Monarch Home Improvements , and the service is amazing! Owen came round several times as we keep changing our minds and he was so helpful and gave us good advice, and the guys who do the fitting are efficient and tidy . I’ve got to say the end result is amazing and I have recommended to many of friends Thanks Monarch Reliablity: 9.38 Courtesy: 10 Tidiness: 9.84 Workmanship: 10</p>
  <div class="author"><svg class="avatar"><use href="#user"/></svg><div><div class="author-name">By Tom, <small>13 Feb 2018</small></div><div class="stars"><svg><use href="#star"/></svg><svg><use href="#star"/></svg><svg><use href="#star"/></svg><svg><use href="#star"/></svg><svg><use href="#star"/></svg></div></div></div>
  <div class="source"><div class="source-name" style="font-size:14px">TrustNest</div><div class="stars"><svg><use href="#star"/></svg><svg><use href="#star"/></svg><svg><use href="#star"/></svg><svg><use href="#star"/></svg><svg><use href="#star"/></svg></div></div>
</article>

<div class="load">LOAD MORE <svg viewBox="0 0 12 12"><circle cx="6" cy="6" r="6" fill="#fff"/><path d="M3.5 5l2.5 2.5L8.5 5" fill="none" stroke="#5a9e2f" stroke-width="1.6"/></svg></div>

<div class="powered"><i></i><div><div class="powered-by">Powered by</div><div class="powered-name">ReviewGather</div></div></div>

<footer class="footer">© 2021&nbsp; Company Name &nbsp;|&nbsp; All Rights Reserved</footer>
</body>
</html>
```